Halvo KT Biz Card Design

Residential / Commercial/ Emergency

Industry/Entity Type

Residential

Contact Information for Business Card

Tomas Welker
President
PO Box 4827
Marlow Cove, NY 11950
tomas@halvo-kt.com
631.555.0172
855.HALVO.KT
www.halvo-kt.com
FB: Halvo KT
Twitter: HALVO KT

```html
<!DOCTYPE html>
<html lang="en">
<head>
<meta charset="utf-8">
<title>Halvo KT Business Card</title>
<link rel="stylesheet" href="https://fonts.googleapis.com/css2?family=Open+Sans:wght@400;600&display=swap">
<style>
  :root {
    --backdrop: #c9c9c9;
    --card-dark: #25292d;
    --card-light: #ffffff;
    --brand-orange: #ee8a24;
    --ring-orange: #e07f22;
    --text-light: #ffffff;
    --text-muted: #b9bcbf;
    --text-dark: #23272b;
  }
  * { box-sizing: border-box; margin: 0; padding: 0; }
  html, body { width: 1200px; height: 800px; overflow: hidden; }
  body {
    background: var(--backdrop);
    font-family: "Open Sans", Arial, sans-serif;
    position: relative;
  }
  .card {
    position: absolute;
    top: 252px;
    width: 520px;
    height: 296px;
    border-radius: 22px;
    overflow: hidden;
    box-shadow: 0 6px 18px rgba(0,0,0,0.25);
  }
  .card-front { left: 60px; background: var(--card-dark); }
  .card-back { left: 620px; background: var(--card-light); }

  .front-band {
    position: absolute; left: 0; top: 0; bottom: 0; width: 44px;
    background: var(--brand-orange);
  }
  .logo-disc {
    position: absolute; left: 28px; top: 38px;
    width: 220px; height: 220px; border-radius: 50%;
    background: var(--card-light);
    border: 9px solid var(--ring-orange);
    display: flex; align-items: center; justify-content: center;
  }
  .brand-name {
    font-weight: 600;
    color: var(--text-dark);
    letter-spacing: 0.06em;
    white-space: nowrap;
  }
  .logo-disc .brand-name { font-size: 24px; }

  .divider {
    position: absolute; left: 268px; top: 36px; bottom: 36px;
    width: 2px; background: var(--brand-orange);
  }
  .contact {
    position: absolute; left: 284px; top: 56px; right: 10px;
  }
  .contact-name {
    font-size: 25px; font-weight: 600; color: var(--brand-orange);
    line-height: 1.1; letter-spacing: 0.01em; white-space: nowrap;
  }
  .contact-title {
    font-size: 14px; font-weight: 600; color: var(--text-light);
    margin-bottom: 16px;
  }
  .contact-list { list-style: none; }
  .contact-item {
    display: flex; align-items: center; gap: 7px;
    font-size: 11px; color: var(--text-muted); line-height: 1.35;
    margin-bottom: 8px; white-space: nowrap;
  }
  .contact-icon { flex: 0 0 12px; width: 12px; height: 12px; }
  .contact-icon * { fill: var(--text-muted); }

  .back-logo {
    position: absolute; left: 0; right: 0; top: 104px;
    text-align: center;
  }
  .back-logo .brand-name { font-size: 52px; line-height: 1; }
  .back-url {
    margin-top: 16px;
    font-size: 19px; color: var(--text-dark); letter-spacing: 0.18em;
  }
</style>
</head>
<body>
  <section class="card card-front" aria-label="Business card front">
    <div class="front-band"></div>
    <div class="logo-disc"><span class="brand-name">HALVO KT</span></div>
    <div class="divider"></div>
    <div class="contact">
      <p class="contact-name">Tomas Welker</p>
      <p class="contact-title">Owner/President</p>
      <ul class="contact-list">
        <li class="contact-item">
          <svg class="contact-icon" viewBox="0 0 12 12" aria-hidden="true"><path d="M6 0a4 4 0 0 0-4 4c0 3 4 8 4 8s4-5 4-8a4 4 0 0 0-4-4zm0 5.6A1.6 1.6 0 1 1 6 2.4a1.6 1.6 0 0 1 0 3.2z"/></svg>
          <span>PO Box 4827 Marlow Cove, NY 11950</span>
        </li>
        <li class="contact-item">
          <svg class="contact-icon" viewBox="0 0 12 12" aria-hidden="true"><path d="M0 2h12v1L6 7 0 3z"/><path d="M0 4.2l6 4 6-4V10H0z"/></svg>
          <span>tomas@halvo-kt.com</span>
        </li>
        <li class="contact-item">
          <svg class="contact-icon" viewBox="0 0 12 12" aria-hidden="true"><path d="M3 0h6a1 1 0 0 1 1 1v10a1 1 0 0 1-1 1H3a1 1 0 0 1-1-1V1a1 1 0 0 1 1-1zm.5 1.5v8h5v-8z"/></svg>
          <span>631.555.0172 855.</span>
        </li>
        <li class="contact-item">
          <svg class="contact-icon" viewBox="0 0 12 12" aria-hidden="true"><path d="M6 0a6 6 0 1 0 0 12A6 6 0 0 0 6 0zm0 1.2c.6.7 1 1.8 1.2 3H4.8c.2-1.2.6-2.3 1.2-3zM1.3 5.4h2.3a9 9 0 0 0 0 1.2H1.3a4.8 4.8 0 0 1 0-1.2zm3.5 2.4h2.4c-.2 1.2-.6 2.3-1.2 3-.6-.7-1-1.8-1.2-3zm3.6-1.2a9 9 0 0 0 0-1.2h2.3a4.8 4.8 0 0 1 0 1.2z"/></svg>
          <span>HALVO.KT www.halvo-kt.com</span>
        </li>
      </ul>
    </div>
  </section>

  <section class="card card-back" aria-label="Business card back">
    <div class="back-logo">
      <span class="brand-name">HALVO KT</span>
      <p class="back-url">www.halvo-kt.com</p>
    </div>
  </section>
</body>
</html>
```